One label design for 3 different sizes of honey bottles

Our honey company -- Amber Hollow Apiary -- needs new product labels, integrating our new name and logo. We would like one label design that presents equally well on three different sizes of plastic honey bottles. Designs should include a front and back label.

Keep in mind that we really like our old label. Please submit designs that have a similar color and font scheme as the old label.

In the uploaded files, you will find (1) detailed content instructions for each size label (2 lb, 1 lb, 8 oz), (2) photo of three plastic bottles without labels, (3) *.ai file for the new company logo, and (4) image of old package label.

Requirements
Must have
• Same look and feel as our old label, but with our new name and logo

```html
<!DOCTYPE html>
<html lang="en">
<head>
<meta charset="utf-8">
<title>Amber Hollow Apiary – Honey Label</title>
<link rel="stylesheet" href="https://fonts.googleapis.com/css2?family=Courier+Prime:wght@400;700&family=Rye&family=Archivo:wght@400;700;800&display=swap">
<style>
  :root {
    --page: #ffffff;
    --label-edge: #f4dfc0;
    --label-cream: #faf3e5;
    --band: #f5e3c6;
    --gold: #c49a3c;
    --gold-light: #e2c677;
    --honey-brown: #a66d22;
    --honey-shadow: #e9cf9a;
    --ink: #2e2616;
    --ribbon-ink: #6b5424;
  }
  * { margin: 0; padding: 0; box-sizing: border-box; }
  html, body { width: 1200px; height: 995px; overflow: hidden; background: var(--page); }
  .canvas { position: relative; width: 1200px; height: 995px; }

  .label {
    position: absolute; top: 42px; width: 511px; height: 899px;
    background: var(--label-edge);
  }
  .label--front { left: 58px; }
  .label--back { left: 630px; }
  .label__panel {
    position: absolute; inset: 14px;
    background: var(--label-cream);
    border: 1.5px solid var(--gold);
    outline: 1px solid var(--gold-light);
    outline-offset: -6px;
  }
  .label__art { position: absolute; inset: 0; width: 511px; height: 899px; }

  .promise {
    position: absolute; top: 70px; left: 30px; width: 451px;
    font: 400 20px/35px "Courier Prime", monospace;
    color: var(--ink); text-align: center; white-space: nowrap;
  }
  .nutrition {
    position: absolute; top: 375px; left: 32px; width: 449px; height: 103px;
    border: 1.5px solid var(--ink); background: #fff;
    padding: 5px 7px; color: #111;
    font: 400 9.5px/12.5px "Archivo", Arial, sans-serif;
    white-space: nowrap; overflow: hidden;
  }
  .nutrition__title { font-weight: 800; font-size: 18px; }
  .nutrition__big { font-weight: 800; font-size: 15px; }
  .nutrition b { font-weight: 700; }
  .nutrition__note { font-size: 6.5px; line-height: 9px; margin-top: 1px; }

  .warning {
    position: absolute; top: 545px; left: 40px; width: 431px;
    font: 400 16px/23px "Courier Prime", monospace;
    color: var(--ink); text-align: center;
  }
  .address {
    position: absolute; top: 778px; left: 30px; width: 451px;
    font: 400 18px/22px "Courier Prime", monospace;
    color: var(--ink); text-align: center; white-space: nowrap;
  }
  .brand {
    position: absolute; left: 40px; width: 431px; text-align: center;
    font-family: "Courier Prime", monospace; font-weight: 700; color: var(--gold);
  }
  .brand__dot { display: block; margin: 0 auto; border-radius: 50%; background: var(--gold); }
  .brand--front { top: 585px; font-size: 34px; line-height: 40px; }
  .brand--front .brand__dot { width: 20px; height: 20px; margin-bottom: 14px; }
  .brand--back { top: 660px; font-size: 17px; line-height: 20px; }
  .brand--back .brand__dot { width: 10px; height: 10px; margin-bottom: 8px; }

  .net-weight {
    position: absolute; top: 816px; left: 120px; width: 271px;
    font: 400 17px/28px "Courier Prime", monospace; color: var(--ink); text-align: center;
  }
</style>
</head>
<body>
<main class="canvas">

  <section class="label label--front" aria-label="Front label">
    <div class="label__panel"></div>
    <svg class="label__art" viewBox="0 0 511 899" xmlns="http://www.w3.org/2000/svg">
      <defs>
        <path id="ribbon-arc" d="M 50 178 Q 256 92 461 178"/>
        <radialGradient id="bee-tone" cx="50%" cy="50%" r="50%">
          <stop offset="0%" stop-color="#d9b055"/>
          <stop offset="100%" stop-color="#faf3e5"/>
        </radialGradient>
      </defs>
      <text font-family="Rye, serif" font-size="25" fill="var(--ribbon-ink)" letter-spacing="1.5" text-anchor="middle">
        <textPath href="#ribbon-arc" startOffset="50%">LOCAL • PURE • RAW</textPath>
      </text>
      <rect x="160" y="180" width="192" height="90" rx="45" fill="url(#bee-tone)" role="img" aria-label="Engraved honey bee illustration"/>
      <line x1="22" y1="272" x2="489" y2="272" stroke="var(--gold)" stroke-width="1.5"/>
      <line x1="22" y1="278" x2="489" y2="278" stroke="var(--gold)" stroke-width="1"/>
      <rect x="30" y="284" width="451" height="218" fill="var(--band)"/>
      <text x="66" y="484" font-family="Rye, serif" font-size="190" fill="var(--honey-shadow)" textLength="392" lengthAdjust="spacingAndGlyphs">HONEY</text>
      <text x="58" y="476" font-family="Rye, serif" font-size="190" fill="var(--honey-brown)" textLength="392" lengthAdjust="spacingAndGlyphs">HONEY</text>
      <line x1="22" y1="507" x2="489" y2="507" stroke="var(--gold)" stroke-width="1"/>
      <line x1="22" y1="513" x2="489" y2="513" stroke="var(--gold)" stroke-width="1.5"/>
      <line x1="120" y1="812" x2="391" y2="812" stroke="var(--gold)" stroke-width="1.2"/>
      <line x1="120" y1="848" x2="391" y2="848" stroke="var(--gold)" stroke-width="1.2"/>
    </svg>
    <div class="brand brand--front"><span class="brand__dot"></span>Amber Hollow<br>Apiary</div>
    <p class="net-weight">Net Wt. 1 LB (454 g)</p>
  </section>

  <section class="label label--back" aria-label="Back label">
    <div class="label__panel"></div>
    <svg class="label__art" viewBox="0 0 511 899" xmlns="http://www.w3.org/2000/svg">
      <line x1="22" y1="526" x2="489" y2="526" stroke="var(--gold)" stroke-width="1.5"/>
      <line x1="22" y1="532" x2="489" y2="532" stroke="var(--gold)" stroke-width="1"/>
      <line x1="22" y1="603" x2="489" y2="603" stroke="var(--gold)" stroke-width="1"/>
      <line x1="22" y1="609" x2="489" y2="609" stroke="var(--gold)" stroke-width="1.5"/>
    </svg>
    <p class="promise">Amber Hollow Apiary promises<br>100% pure honey, never<br>pasteurized, and sourced<br>exclusively from beehives we<br>keep near Hollow Falls,<br>West Virginia</p>
    <div class="nutrition">
      <div><span class="nutrition__title">Nutrition Facts</span> Servings: 16, <b>Serv. size: 1 Tbsp (21g),</b></div>
      <div>Amount per serving: <span class="nutrition__big">Calories 60,</span> <b>Total Fat</b> 0g (0% DV), Sat. Fat 0g (0% DV),</div>
      <div><i>Trans</i> Fat 0g, <b>Cholest.</b> 0mg (0% DV), <b>Sodium</b> 0mg (0% DV), <b>Total Carb.</b> 17g (6% DV),</div>
      <div>Fiber 0g (0% DV), Total Sugars 17g (Incl. 17g Added, 34% DV¹), <b>Protein</b> 0g,</div>
      <div>Vit. D (0% DV), Calcium (0% DV), Iron (0% DV), Potas. (0% DV).</div>
      <div class="nutrition__note">¹ One serving adds 17g of sugar to your diet and represents 34% of the Daily Value for Added Sugars.</div>
    </div>
    <p class="warning">DO NOT FEED HONEY TO INFANTS<br>UNDER ONE YEAR OLD</p>
    <div class="brand brand--back"><span class="brand__dot"></span>Amber Hollow<br>Apiary</div>
    <p class="address">Amber Hollow Apiary<br>18 Linden Ridge Road<br>Hollow Falls, WV 25999<br>www.amberhollowapiary.com</p>
  </section>

</main>
</body>
</html>
```